Kestrel Valley Alpine Riders Society needs a business card design

We need a business card design for our newly incorporated KVARS. We are helping the NZ Chinese community, as well as everyone else, to organise ski & snowboarding trips, training, and equipments. The design should be creative, energetic, young and vibrant.

Industry/Entity Type

Social Club

Contact Information for Business Card

Logo; Kestrel Valley Alpine Riders Society; Name: Oliver Brandt; Position: President; Address: 42 Marwick Rd, Epsom, Auckland 1051; Mobile: 020 7826 1957; Email: oliver@kvars-club.example; Web: www.kvars-club.example

Requirements
Must have
• 1, The text "Kestrel Valley Alpine Riders Society" should be put together with the supplied logo file to form a new complete logo combination.
• 2, Final design files should be in Adobe Illustrator format and all text must be editable.
Nice to have
• two or three colours

```html
<!DOCTYPE html>
<html lang="en">
<head>
<meta charset="utf-8">
<title>KVARS Business Card</title>
<link href="https://fonts.googleapis.com/css2?family=Montserrat:wght@400;500;700;800&display=swap" rel="stylesheet">
<style>
  :root {
    --backdrop: #d1d2d4;
    --card: #ffffff;
    --navy: #2a3378;
    --blue: #1d5fb0;
    --cyan: #22b8ea;
    --text: #2a3275;
  }
  * { box-sizing: border-box; margin: 0; padding: 0; }
  html, body { width: 1200px; height: 927px; overflow: hidden; }
  body {
    background: var(--backdrop);
    font-family: "Montserrat", sans-serif;
    color: var(--text);
    position: relative;
  }
  .card {
    position: absolute;
    left: 266px;
    width: 669px;
    height: 382px;
    background: var(--card);
    border-radius: 16px;
    overflow: hidden;
  }
  .card--front { top: 66px; }
  .card--back { top: 478px; }

  .wordmark {
    position: absolute;
    font-weight: 800;
    color: var(--blue);
    letter-spacing: 1px;
    line-height: 1;
  }
  .card--front .wordmark {
    left: 61px; width: 255px; top: 140px;
    font-size: 66px; text-align: center;
  }
  .org-name {
    position: absolute;
    left: 61px; width: 255px;
    text-align: center;
    font-weight: 500;
    letter-spacing: 0.6px;
    white-space: nowrap;
  }
  .org-name--primary { top: 244px; font-size: 17px; color: var(--navy); }
  .org-name--secondary { top: 266px; font-size: 15px; color: var(--cyan); }

  .divider {
    position: absolute;
    left: 362px; top: 103px;
    width: 2px; height: 183px;
    background: var(--navy);
  }
  .contact { position: absolute; left: 405px; top: 98px; }
  .contact__name {
    font-size: 28px; font-weight: 700; color: var(--blue);
    letter-spacing: 0.5px; line-height: 1;
  }
  .contact__role {
    margin-top: 6px; font-size: 16px; font-weight: 500; color: var(--cyan);
  }
  .contact__address {
    margin-top: 14px; font-size: 17px; line-height: 22px; font-weight: 500;
  }
  .contact__list { list-style: none; margin-top: 12px; }
  .contact__list li {
    display: flex; align-items: center;
    font-size: 17px; font-weight: 500; line-height: 22.5px;
  }
  .contact__list svg { width: 12px; height: 12px; margin-right: 12px; flex: none; }

  .card--back .wordmark {
    left: 0; right: 0; top: 150px;
    text-align: center; font-size: 92px;
  }
  .back-band {
    position: absolute; left: 0; right: 0;
    top: 319px; height: 39px;
    background: var(--cyan);
  }
  .back-pill {
    position: absolute;
    left: 41px; width: 587px;
    top: 315px; height: 47px;
    background: var(--navy);
    border: 4px solid var(--card);
    border-radius: 24px;
    color: #fff;
    font-size: 17.5px; font-weight: 400;
    letter-spacing: 0.8px;
    display: flex; align-items: center; justify-content: center;
    white-space: nowrap;
  }
</style>
</head>
<body>
  <section class="card card--front">
    <div class="wordmark">KVARS</div>
    <div class="org-name org-name--primary">KESTREL VALLEY ALPINE</div>
    <div class="org-name org-name--secondary">RIDERS SOCIETY</div>
    <div class="divider"></div>
    <div class="contact">
      <h1 class="contact__name">OLIVER BRANDT</h1>
      <p class="contact__role">President</p>
      <p class="contact__address">42 Marwick Rd, Epsom,<br>Auckland 1051</p>
      <ul class="contact__list">
        <li>
          <svg viewBox="0 0 12 12" fill="none" stroke="#2a3275" stroke-width="1.3"><rect x="3" y="0.8" width="6" height="10.4" rx="1"/><line x1="5" y1="9.3" x2="7" y2="9.3"/></svg>
          020 7826 1957
        </li>
        <li>
          <svg viewBox="0 0 12 12" fill="none" stroke="#2a3275" stroke-width="1.2"><rect x="0.8" y="2.5" width="10.4" height="7" rx="0.8"/><polyline points="1,3 6,6.8 11,3"/></svg>
          oliver@kvars-club.example
        </li>
        <li>
          <svg viewBox="0 0 12 12" fill="none" stroke="#2a3275" stroke-width="1"><circle cx="6" cy="6" r="5.2"/><ellipse cx="6" cy="6" rx="2.3" ry="5.2"/><line x1="0.8" y1="6" x2="11.2" y2="6"/><line x1="1.6" y1="3.5" x2="10.4" y2="3.5"/><line x1="1.6" y1="8.5" x2="10.4" y2="8.5"/></svg>
          www.kvars-club.example
        </li>
      </ul>
    </div>
  </section>

  <section class="card card--back">
    <div class="wordmark">KVARS</div>
    <div class="back-band"></div>
    <div class="back-pill">KESTREL VALLEY ALPINE RIDERS SOCIETY</div>
  </section>
</body>
</html>
```